We are a printed circuit board manufacturer. Need a company professional web site to allow our potential customers to know more about our background, capability and our products. The web site will contain three languages, which are Chinese, English and Japanese. Our audience are mainly electronic companies that procure printed circuit boards. I have a word document that have all the required text in all three languages. The final design should communicate the impression that we embrace quality, trustworthiness and long term partnership business principles.
We should have sections that allow us to post pictures of our facilities.
I have added the three files in three different languages.
Some of the information is below:
Background
RVT Harbourline Limited (RVT) was set up in Hong Kong in 2007 by two Hong Kong entrepreneurs, Mr. Dao Lanh and Mr. Tai Pak. We acquired the single sided printed circuit board factory located in Dongguan City, Guangdong Province, China, from Tolvane Corporation of the U.S. in 2007. In addition to RVT, Mr. Lanh and Mr. Pak also own Brightwell Technology Company Limited, a semiconductor company based in Hong Kong since 1997 with a total investment of over US$100 million. Brightwell is engaged in the manufacturing of flexible substrates and MEMS assembly business.
RVT has been awarded TS 16949 and ISO14000 certificates since 2009 and 2004 respectively.
Business Principles
RVT Harbourline Limited strives to be a professional top notched printed circuit board supplier. We embrace four “EXCELLENCE” principles, namely, excellence in quality, excellence in prices, excellence in services and excellence in on time delivery.
We approach each customer with a long-term partnership view that delivers the lowest ownership costs and highest total values to our customers. We customize quotations and solutions in order to allow our customers to win more businesses. We believe by thinking from our customers’ points of view we will be able to create a WIN-WIN relationship.
Customers
Due to our excellent quality, services and production systems, RVT Harbourline Limited manage to service a number of large Japanese and US customers, which include:
Technical capability overview
Below is an overview of our current capability:
Target Market(s)
Electronic companies buyers
Industry/Entity Type
Business
Requirements
Must have
- Capability description
Should not have
- no cartoon

```html
<!DOCTYPE html>
<html lang="en">
<head>
<meta charset="utf-8">
<title>RVT Harbourline Limited</title>
<link href="https://fonts.googleapis.com/css2?family=Open+Sans:wght@400;600&family=Ubuntu:wght@400;500&family=Kreon:wght@400&family=Crimson+Text&display=swap" rel="stylesheet">
<style>
:root{
  --green:#0d7a4c;
  --green-dark:#08613b;
  --green-text:#1d7d4a;
  --yellow:#ffc20e;
  --ink:#333;
  --muted:#9a9a9a;
  --body:#555;
  --line:#d9d9d9;
  --footer-top:#1b1b1b;
  --footer-bottom:#3a3a3a;
}
*{margin:0;padding:0;box-sizing:border-box}
html,body{width:982px;height:1200px;overflow:hidden;background:#fff}
body{position:relative;font-family:"Open Sans",Arial,sans-serif;color:var(--ink)}
h1,h2,h3{font-weight:400}
.abs{position:absolute}
ul{list-style:none}

.top-rule{left:0;top:0;width:491px;height:2px;background:var(--green-dark)}
.brand{left:109px;top:20px;display:flex;align-items:center;gap:8px}
.brand-mark{width:18px;height:18px;background:var(--green)}
.brand-name{font-family:"Ubuntu",sans-serif;font-weight:500;font-size:17px;color:var(--green);line-height:1.15}
.contact-top{left:720px;top:27px;font-family:"Ubuntu",sans-serif;font-size:12px;color:#444}
.contact-top div{display:flex;align-items:center;gap:9px;height:22px}
.ico{width:17px;height:17px;border-radius:3px}

.hero{left:0;top:90px;width:982px;height:364px;background:linear-gradient(135deg,#f4f4f4 0%,#e6e6e6 55%,#dcdcdc 100%)}
.hero-photo{left:442px;top:0;width:540px;height:364px;background:radial-gradient(ellipse at 60% 45%,#d98a2c 0%,#c26f1e 40%,#8b5a2b 70%,#dcdcdc 100%)}
.nav{left:91px;top:90px;width:797px;height:37px;background:linear-gradient(#12875a,var(--green-dark));display:flex;align-items:center;padding-left:19px;font-size:10.6px;color:#fff}
.nav a{color:#fff;text-decoration:none;margin-right:26.5px}
.nav .sel{position:absolute;top:8px;width:31px;height:22px;background:#fff;border-radius:2px}
.hero-title{left:93px;top:230px;width:360px;font-family:"Kreon",serif;font-weight:400;font-size:21px;line-height:27px;color:var(--green-text)}
.btn{left:93px;top:321px;width:80px;height:29px;background:var(--yellow);border:1px solid #e0a800;color:#5a3a00;font-size:11.5px;display:flex;align-items:center;justify-content:center}

.clients{left:0;top:454px;width:982px;height:60px;background:linear-gradient(#fff,#ececec);border-top:1px solid #ddd;border-bottom:1px solid #ccc}
.clients-tab{left:90px;top:450px;width:164px;height:49px;background:#1a1a1a;border-radius:4px 4px 3px 3px;color:#fff;font-family:"Ubuntu",sans-serif;font-weight:500;font-size:11.5px;display:flex;align-items:center;justify-content:center}
.client{top:475px;font-family:"Ubuntu",sans-serif;font-weight:500;font-size:18px}
.testimonials{left:407px;top:514px;width:212px;height:29px;background:linear-gradient(#f3f3f3,#dedede);border:1px solid #ccc;border-top:0;border-radius:0 0 8px 8px;font-family:"Ubuntu",sans-serif;font-size:12px;color:#333;display:flex;align-items:center;justify-content:center;gap:9px}
.testimonials span.dot{width:17px;height:17px;border-radius:50%;background:#666;display:flex;align-items:center;justify-content:center}

.welcome-title{left:92px;top:548px;font-family:"Open Sans",sans-serif;font-weight:400;font-size:22.5px;color:#444}
.welcome-text{left:93px;top:584px;width:500px;font-size:8.6px;line-height:12.3px;color:var(--body)}
.welcome-cert{left:93px;top:665px;font-size:10px;color:#666;letter-spacing:.2px}

.services{left:91px;top:702px;width:506px;height:215px;border:1px solid #cfcfcf;border-radius:3px;background:linear-gradient(#fff,#e6e6e6)}
.services-head{height:38px;background:linear-gradient(#10865a,var(--green-dark));color:#fff;font-family:"Ubuntu",sans-serif;font-size:16px;padding:9px 8px;border-radius:2px 2px 0 0}
.services-photo{position:absolute;left:9px;top:54px;width:118px;height:90px;border:1px solid #bbb;padding:3px;background:#fff}
.services-photo div{width:100%;height:100%;background:linear-gradient(135deg,#3d7a52,#cfd6d3 60%,#8aa0a0)}
.services-text{position:absolute;left:135px;top:52px;width:350px;font-size:9.6px;line-height:14.7px;color:#666}
.services-text p+p{margin-top:14px}
.services-more{position:absolute;right:13px;bottom:5px;font-size:8.5px;font-style:italic;text-decoration:underline;color:#555}

.aside-title{left:646px;top:551px;width:245px;font-family:"Crimson Text",serif;font-weight:400;font-size:19px;color:#555;border-bottom:1px solid var(--line);padding-bottom:2px}
.item{left:643px;width:249px;height:68px;border-bottom:1px solid var(--line)}
.item .thumb{position:absolute;left:0;top:0;width:53px;height:51px}
.item h3{position:absolute;left:59px;top:-2px;font-family:"Ubuntu",sans-serif;font-weight:400;font-size:12px;color:var(--green-text)}
.item p{position:absolute;left:59px;top:14px;width:192px;font-size:8.3px;line-height:11.5px;color:var(--muted)}
.item .sub{color:var(--green-text);font-size:8.5px}

.footer{left:0;top:946px;width:982px;height:214px;background:linear-gradient(var(--footer-top),var(--footer-bottom));border-top:2px solid #111}
.f-head{font-family:"Ubuntu",sans-serif;font-weight:400;font-size:17px;color:#fff;top:963px}
.f-list{font-family:Arial,sans-serif;font-size:10px;color:#ccc}
.f-list li{height:18.8px;position:relative;padding-left:10px}
.f-list li::before{content:"";position:absolute;left:0;top:5px;width:3px;height:3px;border-radius:50%;background:#ccc}
.social li{display:flex;align-items:center;gap:15px;height:28.6px;font-family:Arial,sans-serif;font-size:10.5px;color:#fff}
.social .sq{width:25px;height:25px;border-radius:3px}
.f-contact{font-family:Arial,sans-serif;font-size:10.5px;line-height:14.8px;color:#fff}
.copyright{left:0;top:1172px;width:1025px;text-align:center;font-size:8.5px;color:#222}
</style>
</head>
<body>
<div class="abs top-rule"></div>
<header>
  <div class="abs brand"><span class="brand-mark"></span><span class="brand-name">RVT<br>Harbourline Limited</span></div>
  <div class="abs contact-top">
    <div><svg class="ico" viewBox="0 0 17 17"><rect width="17" height="17" rx="3" fill="#2ca53c"/><path d="M5 4c1 0 2 2 1.6 2.6L6 7.3c.6 1.5 2 2.9 3.5 3.5l.7-.6c.6-.4 2.6.6 2.6 1.6 0 1-1.3 1.6-2.4 1.4C7.6 12.7 4.3 9.4 3.6 6.6 3.4 5.4 4 4 5 4z" fill="#fff"/></svg>Call Now: (852) 24609183</div>
    <div><svg class="ico" viewBox="0 0 17 17"><rect x="1" y="3" width="15" height="11" fill="#cfe0ef" stroke="#8aa9c4"/><path d="M1 3l7.5 6L16 3" fill="none" stroke="#8aa9c4"/></svg>Email: Sales@rvtboard.com</div>
  </div>
</header>

<section class="abs hero">
  <div class="abs hero-photo" role="img" aria-label="Photo of an assembled printed circuit board with capacitors and a transformer over a schematic drawing"></div>
</section>
<nav class="abs nav">
  <a>Home</a><a>About Us</a><a>Workshop</a><a>Technology</a><a>Feedback</a><a>Accessories</a><a>Customer Service</a><a>Reviews</a><a>Contact Us</a>
  <span class="sel" style="left:721px"></span><span class="sel" style="left:760px"></span>
</nav>
<h1 class="abs hero-title">RVT is providing a RISK FREE supply of double sided and multi-layered printed circuit boards to our customers</h1>
<div class="abs btn">Read More</div>

<div class="abs clients"></div>
<div class="abs clients-tab">Japanese and US customers</div>
<span class="abs client" style="left:262px;color:#1a4ea0">Quenrix</span>
<span class="abs client" style="left:385px;color:#d8232a">DALVORN</span>
<span class="abs client" style="left:487px;color:#1e8a4a">Ostrila</span>
<span class="abs client" style="left:585px;color:#222">KAMIRETH</span>
<span class="abs client" style="left:697px;color:#5a4fb0">velunta</span>
<span class="abs client" style="left:820px;color:#111">ZORVEK</span>
<div class="abs testimonials">View our client testimonials<span class="dot"><svg width="9" height="6" viewBox="0 0 9 6"><path d="M0 0h9L4.5 6z" fill="#fff"/></svg></span></div>

<main>
  <h2 class="abs welcome-title">Welcome to RVT Harbourline</h2>
  <p class="abs welcome-text">RVT Harbourline Limited (RVT) was set up in Hong Kong in 2007 by two Hong Kong entrepreneurs, Mr. Dao Lanh and Mr. Tai Pak. We acquired the single sided printed circuit board factory located in Dongguan City, Guangdong Province, China, from Tolvane Corporation of the U.S. in 2007. In addition to RVT, Mr. Lanh and Mr. Pak also own Brightwell Technology Company Limited, a semiconductor company based in Hong Kong since 1997 with a total investment of over US$100 million. Brightwell is engaged in the manufacturing of flexible substrates and the assembly of Micro Electro Mechanical Systems (MEMS).</p>
  <p class="abs welcome-cert">RVT has been awarded TS 16949 and ISO14000 certificates since 2009 and 2004 respectively.</p>

  <section class="abs services">
    <div class="services-head">About Services</div>
    <div class="services-photo"><div role="img" aria-label="Photo of a technician inspecting boards on the factory floor"></div></div>
    <div class="services-text">
      <p>Our own personnel are stationed at the manufacturers' production facilities 24 hours a day 7 days a week. We provide real time update on a part number by part number basis of our customers' purchase orders status online.</p>
      <p>We examine and test 100% of boards at our own facilities before we deliver to our customers. We provide warehousing services for our customers to ensure products are delivered on a just in time basis.<br>In summary, we help our customers manage their RISKS in procuring printed circuit boards.</p>
    </div>
    <span class="services-more">Read More</span>
  </section>

  <h2 class="abs aside-title">You may also like...</h2>
  <div class="abs item" style="top:587px"><div class="thumb" role="img" aria-label="Photo of a green field under a pale sky" style="background:linear-gradient(#cfe0e8,#9bb566 55%,#c9a94a)"></div><h3>Raw Materials</h3><p>Lorem Ipsum is simply dummy text of the printing and typesetting industry. Lorem Ipsum has been the industry's standard dummy text</p></div>
  <div class="abs item" style="top:654px"><div class="thumb" role="img" aria-label="Photo of copper wires" style="background:linear-gradient(135deg,#fff,#e9b07a 50%,#c0642a)"></div><h3>Copper Thickness</h3><p><span class="sub">double slide</span><br>Lorem Ipsum is simply dummy text of the printing and typesetting industry. Lorem Ipsum</p></div>
  <div class="abs item" style="top:723px"><div class="thumb" role="img" aria-label="Photo of a plating line" style="background:linear-gradient(135deg,#8a9aa8,#d8dde2 50%,#6d7d8a)"></div><h3>Plating</h3><p>Lorem Ipsum is simply dummy text of the printing and typesetting industry. Lorem Ipsum has been the industry's standard dummy text</p></div>
  <div class="abs item" style="top:791px"><div class="thumb" role="img" aria-label="Photo of a CNC drilling machine" style="background:linear-gradient(135deg,#b8bec4,#6d757c 50%,#e2e5e8)"></div><h3>Punching And CNC Process</h3><p>Lorem Ipsum is simply dummy text of the printing and typesetting industry. Lorem Ipsum has been the industry's standard dummy text</p></div>
  <div class="abs item" style="top:860px"><div class="thumb" role="img" aria-label="Photo of green circuit board traces" style="background:linear-gradient(135deg,#2f8f3a,#7fd05a 55%,#2e7a30)"></div><h3>V-Cut</h3><p>Lorem Ipsum is simply dummy text of the printing and typesetting industry. Lorem Ipsum has been the industry's standard dummy text</p></div>
</main>

<footer>
  <div class="abs footer"></div>
  <h3 class="abs f-head" style="left:92px">Quick Links</h3>
  <ul class="abs f-list" style="left:90px;top:995px"><li>Home</li><li>About Us</li><li>Custom Engering</li><li>Automation</li><li>Workshop</li><li>About</li><li>Contact</li></ul>
  <ul class="abs f-list" style="left:284px;top:994px"><li>Featured Product</li><li>Accumulation Tables</li><li>Slicer Project</li><li>Raw Materials</li><li>Punching and CNC Process</li><li>Engineering / Design Assistance</li><li>Platforms</li></ul>
  <h3 class="abs f-head" style="left:499px">Follow Us</h3>
  <ul class="abs social" style="left:501px;top:997px">
    <li><span class="sq" style="background:#3b5a9a"></span>Follow us on Friendwall</li>
    <li><span class="sq" style="background:#4aa8d8"></span>Follow us on Chirpline</li>
    <li><span class="sq" style="background:#1c6ea4"></span>Follow us on Workchain</li>
    <li><span class="sq" style="background:#c8201e"></span>Follow us on Clipstream</li>
  </ul>
  <h3 class="abs f-head" style="left:713px">Contact</h3>
  <div class="abs f-contact" style="left:715px;top:989px;width:140px">RVT Harbourline Limited<br>32/F Lotus Plaza<br>18 Kestrel Avenue<br>Quarry Point, HONG KONG<br><br>Telephone: (852)24609183<br>Fax: (852)24609184<br><br>Email: Sales@rvtboard.com</div>
  <p class="abs copyright">COPYRIGHT - include a copyright statement © 2012 RVT Harbourline Limited, | All rights reserved</p>
</footer>
</body>
</html>
```